Release Therapy business card that deals with the release of negative issues

I need a business card for my business called PEBBLES (A warm hearth to rest when you tire) ... I'm a therapist that deals with people releasing negative issues, by applying therapies that incorporate, hypnosis, aromatherapy and listen therapy..I like the colour green and soft blues...My idea is for a hand releasing butterflies, and incorporating soft clouds....
Target Market(s)
All people, all ages
Industry/Entity Type
Business
Contact Information for Business Card
PEBBLES"A Warm Hearth To Rest When You Tire"Yvette R BrockingtonRelease Therapist0411 743 781email: calmingpaths4you@quietmail.example
Requirements
Must have
- butterflies and soft clouds
Nice to have
- I like the decorative and script fonts for business name, and also my name
- Marisol T Fenwhistle...

```html
<!DOCTYPE html>
<html lang="en">
<head>
<meta charset="utf-8">
<title>PEBBLES – Release Therapy Business Card</title>
<link rel="stylesheet" href="https://fonts.googleapis.com/css2?family=Arimo:wght@700&family=Playfair+Display:wght@800&family=Roboto+Condensed:wght@400&family=Yanone+Kaffeesatz:wght@400&display=swap">
<style>
  :root {
    --sky-top: #86cdf0;
    --sky-mid: #e9f6fb;
    --meadow-light: #cfe88a;
    --meadow: #9cca3a;
    --teal: #1c9c82;
    --brand-green: #7ab317;
    --outline-green: #3f7d12;
    --deep-green: #1f5a3a;
    --ink: #111;
    --white: #fff;
  }
  * { margin: 0; padding: 0; box-sizing: border-box; }
  html, body { width: 1025px; height: 1200px; overflow: hidden; background: var(--white); }
  .canvas { position: relative; width: 1025px; height: 1200px; }

  .card {
    position: absolute; left: 31px; width: 959px; height: 574px; overflow: hidden;
    background: linear-gradient(180deg, var(--sky-top) 0%, var(--sky-mid) 58%, var(--meadow-light) 78%, var(--meadow) 100%);
  }
  .card--front { top: 23px; }
  .card--back { top: 614px; }

  .meadow-band { position: absolute; right: 0; bottom: 0; width: 959px; height: 574px; }

  .brand-name {
    position: absolute; left: 31px; top: 38px;
    font-family: "Playfair Display", serif; font-weight: 800;
    font-size: 84px; line-height: 1; letter-spacing: -2px;
    color: var(--brand-green);
  }
  .tagline {
    position: absolute; left: 42px; top: 148px;
    font-family: "Yanone Kaffeesatz", sans-serif; font-size: 46px; line-height: 1;
    color: var(--white); -webkit-text-stroke: 1.4px var(--outline-green);
    white-space: nowrap;
  }
  .hand-butterflies {
    position: absolute; left: 615px; top: 10px; width: 330px; height: 290px;
    border-radius: 40px;
    background: radial-gradient(ellipse at 65% 50%, #f2b98f 0%, #e9a27a 35%, rgba(140,205,240,0.4) 72%, rgba(140,205,240,0) 100%);
  }

  .holder-name {
    font-family: "Arimo", sans-serif; font-weight: 700;
    font-size: 66px; line-height: 1; color: var(--brand-green); white-space: nowrap;
  }
  .holder-role, .phone {
    font-family: "Roboto Condensed", sans-serif; font-size: 50px; line-height: 1; color: var(--ink); white-space: nowrap;
  }
  .front-line { position: absolute; left: 0; right: 0; text-align: center; }
  .front-name { top: 290px; padding-left: 40px; }
  .front-role { top: 358px; padding-left: 20px; }
  .front-phone { top: 410px; padding-left: 20px; font-family: "Yanone Kaffeesatz", sans-serif; font-size: 56px; }

  .email-row {
    position: absolute; left: 88px; top: 478px; display: flex; align-items: center; gap: 12px;
  }
  .email-icon { width: 56px; height: 56px; }
  .email-text {
    font-family: "Yanone Kaffeesatz", sans-serif; font-size: 54px; line-height: 1;
    color: var(--white); -webkit-text-stroke: 1.4px var(--deep-green); white-space: nowrap;
  }

  .services {
    position: absolute; left: 32px; right: 30px; top: 40px;
    font-family: "Roboto Condensed", sans-serif; font-size: 32px; line-height: 38px;
    color: var(--deep-green); text-align: justify; text-align-last: left;
  }
  .notes-panel {
    position: absolute; left: 31px; top: 129px; width: 898px; height: 273px;
    background: rgba(255,255,255,0.78); border-radius: 9px;
  }
  .back-details { position: absolute; right: 52px; top: 412px; text-align: right; }
  .back-details .holder-role { margin-top: 6px; }
</style>
</head>
<body>
<main class="canvas">
  <section class="card card--front">
    <svg class="meadow-band" viewBox="0 0 959 574" aria-hidden="true">
      <path d="M959 440 C900 500 860 540 800 574 L870 574 C910 530 940 490 959 470 Z" fill="var(--teal)" opacity="0.9"/>
      <path d="M0 545 C200 480 420 565 620 530" fill="none" stroke="#ffffff" stroke-opacity="0.5" stroke-width="3"/>
    </svg>
    <h1 class="brand-name">PEBBLES</h1>
    <p class="tagline">A Warm Hearth To Rest When You Tire</p>
    <div class="hand-butterflies" role="img" aria-label="Open hand releasing colourful butterflies into the sky"></div>
    <p class="front-line front-name holder-name">Marisol T. Fenwhistle</p>
    <p class="front-line front-role holder-role">Release Therapist</p>
    <p class="front-line front-phone phone">0482 516 904</p>
    <div class="email-row">
      <svg class="email-icon" viewBox="0 0 56 56" aria-hidden="true">
        <rect x="2" y="2" width="52" height="52" rx="8" fill="#6cbf1e"/>
        <rect x="11" y="16" width="34" height="24" rx="2" fill="#fff"/>
        <path d="M11 17 L28 31 L45 17" fill="none" stroke="#6cbf1e" stroke-width="2.5"/>
      </svg>
      <span class="email-text">E-Mail: calmingpaths4you@quietmail.example</span>
    </div>
  </section>

  <section class="card card--back">
    <svg class="meadow-band" viewBox="0 0 959 574" aria-hidden="true">
      <path d="M959 430 C910 490 880 540 840 574 L900 574 C930 530 950 480 959 460 Z" fill="var(--teal)" opacity="0.9"/>
      <path d="M0 520 C200 460 400 560 640 510" fill="none" stroke="#ffffff" stroke-opacity="0.5" stroke-width="3"/>
    </svg>
    <p class="services">By applying therapies that incorporate, hypnosis, aromatherapy and listen therapy</p>
    <div class="notes-panel"></div>
    <div class="back-details">
      <p class="holder-name">Marisol T Fenwhistle</p>
      <p class="holder-role">Release Therapist</p>
    </div>
  </section>
</main>
</body>
</html>
```